Banner Ad to promote Youth Cycling Camps

We need a 728 x 90 banner ad to promote some youth cycling camps. There are 2 different camps - a road camp where they learn to ride their bikes on the roads and a mountain bike camp. The camps teach bike handling skills and racing tactics.

Target Market(s)

Parents of youth ages 7-17

Industry/Entity Type

Non-Profit

Font styles to use
Sans Serif

Requirements
Must have
• Logo
• Dates - Road Camp May 5-7, 2017
• - Mountain Bike Camp July 14-16, 2017
• website - pedalwaycircuit.org
• be 728 x 90
Nice to have
• Animated - would like it to rotate with 3 slides - 1 a focus on both camps, 1 on road camp, 1 on mountain bike camp

```html
<!DOCTYPE html>
<html lang="en">
<head>
<meta charset="utf-8">
<title>Youth Cycling Camps – Banner Set</title>
<link rel="stylesheet" href="https://fonts.googleapis.com/css2?family=Open+Sans:ital,wght@0,400;0,600;0,700;0,800;1,700&display=swap">
<style>
  :root {
    --page-bg: #ffffff;
    --panel-green: #84bd1f;
    --accent-yellow: #f4e716;
    --bar-blue: #1b4f86;
    --badge-blue: #70c8ec;
    --badge-ring: #163a5c;
    --text-white: #ffffff;
    --text-navy: #163a5c;
  }
  * { box-sizing: border-box; margin: 0; padding: 0; }
  html, body {
    width: 1200px; height: 537px; overflow: hidden;
    background: var(--page-bg);
    font-family: "Open Sans", Arial, sans-serif;
  }
  .banner-set { position: relative; width: 1200px; height: 537px; }
  .banner {
    position: absolute; left: 38px; width: 1092px; height: 135px;
    overflow: hidden; background: var(--panel-green);
  }
  .banner--camps { top: 30px; }
  .banner--road { top: 192px; }
  .banner--mtb { top: 354px; }

  .banner__photo { position: absolute; left: 0; top: 0; width: 480px; height: 135px; }
  .banner--camps .banner__photo { background: linear-gradient(90deg, #9aa3a8 0%, #c2504a 35%, #3d4a6a 60%, #b7bdc0 100%); }
  .banner--road .banner__photo { background: linear-gradient(180deg, #4f5b46 0%, #6a7560 45%, #a7a7a2 75%, #7c7a6f 100%); }
  .banner--mtb .banner__photo { background: linear-gradient(120deg, #3b3a35 0%, #7f6f5a 40%, #4c5a48 70%, #a59a80 100%); }

  .banner__divider { position: absolute; left: 440px; top: 0; width: 80px; height: 135px; }

  .banner__message {
    position: absolute; left: 484px; top: 0; width: 482px; height: 99px;
    display: flex; flex-direction: column; justify-content: center; align-items: center;
    text-align: center; color: var(--text-white); white-space: nowrap;
  }
  .banner__headline {
    font-size: 26px; font-weight: 700; letter-spacing: -0.3px; line-height: 1.1;
  }
  .banner__headline--light { font-weight: 400; }
  .banner--mtb .banner__headline { font-size: 24px; letter-spacing: -0.4px; }
  .banner__highlight { color: var(--accent-yellow); font-weight: 700; }
  .banner__sub {
    margin-top: 4px; font-size: 17px; font-weight: 700; font-style: italic; line-height: 1.2;
  }
  .banner__quote {
    margin-top: 8px; font-size: 17px; font-weight: 700; font-style: italic;
  }

  .banner__bar {
    position: absolute; left: 490px; right: 0; bottom: 0; height: 36px;
    background: var(--bar-blue); color: var(--text-white);
    display: flex; align-items: center; padding-left: 66px;
    font-size: 17px; letter-spacing: 1.2px; font-weight: 400; white-space: nowrap;
  }
  .banner__bar strong { font-weight: 800; margin-left: 8px; }

  .badge {
    position: absolute; right: 2px; top: 2px; width: 131px; height: 131px;
    border-radius: 50%; background: var(--badge-blue);
    border: 5px solid var(--badge-ring);
    display: flex; align-items: center; justify-content: center; text-align: center;
  }
  .badge__name {
    color: var(--text-navy); font-weight: 800; font-size: 15px; line-height: 1.15;
    letter-spacing: 0.5px;
  }
</style>
</head>
<body>
<main class="banner-set">

  <section class="banner banner--camps">
    <div class="banner__photo" role="img" aria-label="Group photo of youth cyclists in team jerseys and helmets"></div>
    <svg class="banner__divider" viewBox="0 0 80 135" aria-hidden="true">
      <path d="M80 0 H46 Q20 67 48 135 H80 Z" fill="var(--panel-green)"/>
      <path d="M46 0 Q20 67 48 135" fill="none" stroke="var(--accent-yellow)" stroke-width="10"/>
    </svg>
    <div class="banner__message">
      <p class="banner__headline">BEST CYCLING CAMPS <span class="banner__headline--light">FOR</span> <span class="banner__highlight">AGES 7-17</span></p>
      <p class="banner__sub">Professional Coaches, great youth<br>to adult ratio, affordable</p>
    </div>
    <div class="banner__bar">VISIT US AT <strong>PEDALWAYCIRCUIT.ORG</strong></div>
    <div class="badge"><span class="badge__name">PEDALWAY<br>CIRCUIT</span></div>
  </section>

  <section class="banner banner--road">
    <div class="banner__photo" role="img" aria-label="Young riders racing in a group on a forest road"></div>
    <svg class="banner__divider" viewBox="0 0 80 135" aria-hidden="true">
      <path d="M80 0 H46 Q20 67 48 135 H80 Z" fill="var(--panel-green)"/>
      <path d="M46 0 Q20 67 48 135" fill="none" stroke="var(--accent-yellow)" stroke-width="10"/>
    </svg>
    <div class="banner__message">
      <p class="banner__headline banner__headline--light">ROAD CAMP – <span class="banner__highlight">MAY 5-7, 2017</span></p>
      <p class="banner__quote">„Well organized, great coaches, good location“</p>
    </div>
    <div class="banner__bar">VISIT US AT <strong>PEDALWAYCIRCUIT.ORG</strong></div>
    <div class="badge"><span class="badge__name">PEDALWAY<br>CIRCUIT</span></div>
  </section>

  <section class="banner banner--mtb">
    <div class="banner__photo" role="img" aria-label="Kids on mountain bikes riding a dirt trail"></div>
    <svg class="banner__divider" viewBox="0 0 80 135" aria-hidden="true">
      <path d="M80 0 H46 Q20 67 48 135 H80 Z" fill="var(--panel-green)"/>
      <path d="M46 0 Q20 67 48 135" fill="none" stroke="var(--accent-yellow)" stroke-width="10"/>
    </svg>
    <div class="banner__message">
      <p class="banner__headline banner__headline--light">MOUNTAIN BIKE CAMP – <span class="banner__highlight">JULY 14-16, 2017</span></p>
      <p class="banner__quote">„Good mix of skill building exercises and just riding“</p>
    </div>
    <div class="banner__bar">VISIT US AT <strong>PEDALWAYCIRCUIT.ORG</strong></div>
    <div class="badge"><span class="badge__name">PEDALWAY<br>CIRCUIT</span></div>
  </section>

</main>
</body>
</html>
```